Need a banner for trees, and shrubs at our lanscape supply yard see attached logo

Need a nice banner to showcase our new addition of trees and shrubs for our customers.

```html
<!DOCTYPE html>
<html lang="en">
<head>
<meta charset="utf-8">
<title>Trees and Shrubs Banner</title>
<link href="https://fonts.googleapis.com/css2?family=Oswald:wght@500&display=swap" rel="stylesheet">
<style>
  :root {
    --page: #ececec;
    --maroon-deep: #3f0c09;
    --maroon: #6a1b13;
    --band-red: #5a150f;
    --hedge-dark: #1d5f1f;
    --hedge-mid: #2f862b;
    --shrub-light: #9ad34a;
    --shrub-mid: #4f9e2c;
    --field-top: #6aa54a;
    --field-mid: #4a8f34;
    --field-low: #6cae3e;
    --banner-green: #0c9a49;
    --white: #ffffff;
  }
  * { margin: 0; padding: 0; box-sizing: border-box; }
  html, body {
    width: 1200px;
    height: 1200px;
    overflow: hidden;
    background: var(--page);
  }
  .canvas {
    width: 1200px;
    height: 1200px;
    display: flex;
    align-items: center;
    justify-content: center;
  }
  .banner {
    width: 1020px;
    height: 550px;
    display: block;
    box-shadow: 0 2px 6px rgba(0,0,0,0.25);
  }
  .headline {
    font-family: "Oswald", "Arial Narrow", sans-serif;
    font-weight: 500;
    fill: var(--white);
    text-anchor: middle;
  }
  .brand-name {
    font-family: "Oswald", "Arial Narrow", sans-serif;
    font-weight: 500;
    fill: var(--white);
  }
</style>
</head>
<body>
<main class="canvas">
  <svg class="banner" viewBox="0 0 816 440" xmlns="http://www.w3.org/2000/svg" aria-label="Trees and shrubs banner">
    <defs>
      <radialGradient id="maroonPhoto" cx="0.75" cy="0.35" r="0.8">
        <stop offset="0" stop-color="var(--maroon)"/>
        <stop offset="1" stop-color="var(--maroon-deep)"/>
      </radialGradient>
      <linearGradient id="hedgePhoto" x1="0" y1="0" x2="0.3" y2="1">
        <stop offset="0" stop-color="var(--hedge-dark)"/>
        <stop offset="1" stop-color="var(--hedge-mid)"/>
      </linearGradient>
      <linearGradient id="shrubPhoto" x1="0" y1="0" x2="1" y2="1">
        <stop offset="0" stop-color="var(--shrub-light)"/>
        <stop offset="1" stop-color="var(--shrub-mid)"/>
      </linearGradient>
      <linearGradient id="fieldPhoto" x1="0" y1="0" x2="0" y2="1">
        <stop offset="0" stop-color="var(--field-top)"/>
        <stop offset="0.45" stop-color="var(--field-mid)"/>
        <stop offset="1" stop-color="var(--field-low)"/>
      </linearGradient>
    </defs>

    <rect class="garden-photo-backdrop" width="816" height="440" fill="url(#maroonPhoto)"
          role="img" aria-label="Photo of a garden bench among shrubs, tinted deep red"/>

    <polygon class="hedge-photo" points="88,0 528,0 423,180 383,178" fill="url(#hedgePhoto)"
             role="img" aria-label="Photo of a trimmed green hedge under trees"/>

    <polygon class="diagonal-band" points="0,0 88,0 742,375 704,375 0,8" fill="var(--band-red)"/>

    <polygon class="shrub-photo" points="540,48 423,172 742,376" fill="url(#shrubPhoto)"
             role="img" aria-label="Close-up photo of a leafy rounded shrub"/>

    <polygon class="topiary-photo" points="0,8 383,218 0,430" fill="url(#fieldPhoto)"
             role="img" aria-label="Photo of a nursery field of conical topiary trees and lavender"/>

    <polygon class="title-panel" points="38,440 391,240 733,440" fill="var(--banner-green)"/>

    <text class="headline" x="381" y="342" font-size="48">TREES</text>
    <text class="headline" x="381" y="400" font-size="48">AND SHRUBS</text>

    <g class="brand">
      <circle class="brand-dot" cx="628" cy="64" r="9" fill="var(--white)"/>
      <text class="brand-name" x="644" y="73" font-size="26">FIELDWAY</text>
      <text class="brand-name" x="646" y="96" font-size="13" letter-spacing="5">SUPPLY</text>
    </g>
  </svg>
</main>
</body>
</html>
```